Brenner Business Cards

Front of business card will have logo, name, address, & telephone number. Back of card will have a list of services provided - Roads, Substation Pads, Temporary Pads, Site Pads, Land Leveling, Powerline Row Cleaning, Land Clearing, Gates, Fencing, Construction Entrances, Excavation, Trenching, Underground Utilities, Directional Boring, Pile Driving. We are a construction company that uses heavy equipment like bulldozers, motor graders/blades, dump trucks, backhoes, hydro axes, & skid loaders. We build roads, pads, & install electric utility lines & waterlines underground. This logo is new. The word "Construction" can be smaller as uploaded 2 example edited logos. We will be using this card design for many employees.
Target Market(s)
Industrial Electric Powerline, Wind Turbine, Solar Panel, & Water Utility companies.
Contact Information for Business Card
Name/Position - Danny Brenner - Owner
Address: 4837 FM 952
Halden, TX 79284
Phone number - (325) 518-2906

```html
<!DOCTYPE html>
<html lang="en">
<head>
<meta charset="utf-8">
<title>Brenner Construction Business Cards</title>
<link rel="stylesheet" href="https://fonts.googleapis.com/css2?family=Marcellus&display=swap">
<style>
  :root {
    --maroon: #3d131c;
    --paper: #ffffff;
    --backdrop: #e9e7e6;
    --rule-grey: #6b6b6b;
  }
  * { box-sizing: border-box; margin: 0; padding: 0; }
  html, body { width: 1200px; height: 895px; overflow: hidden; }
  body {
    background: var(--backdrop);
    font-family: "Marcellus", Georgia, serif;
    position: relative;
  }
  .card {
    position: absolute;
    width: 600px;
    height: 343px;
    border-radius: 4px;
    overflow: hidden;
    box-shadow: 0 6px 18px rgba(0,0,0,0.18);
  }
  .card-back {
    left: 90px; top: 90px;
    background: var(--maroon);
    color: var(--paper);
  }
  .service-list {
    position: absolute;
    left: 34px; top: 40px;
    list-style: none;
  }
  .service-list li {
    font-size: 13.5px;
    line-height: 18px;
    letter-spacing: 0.4px;
    display: flex;
    align-items: center;
    white-space: nowrap;
  }
  .service-list li::before {
    content: "";
    width: 7px; height: 7px;
    background: var(--paper);
    margin-right: 10px;
    flex: none;
  }
  .brand {
    position: absolute;
    text-align: center;
    text-transform: uppercase;
    line-height: 1;
  }
  .brand-name { display: block; font-size: 40px; letter-spacing: 3px; }
  .brand-sub { display: block; font-size: 22px; letter-spacing: 2px; margin-top: 8px; }
  .card-back .brand { left: 300px; top: 110px; width: 270px; color: var(--paper); }

  .card-front {
    left: 510px; top: 460px;
    background: var(--paper);
    color: var(--maroon);
  }
  .front-band {
    position: absolute;
    left: 0; right: 0; bottom: 0;
    height: 58px;
    background: var(--maroon);
  }
  .card-front .brand { left: 40px; top: 135px; width: 270px; color: var(--maroon); }
  .divider {
    position: absolute;
    left: 340px; top: 40px;
    width: 1px; height: 180px;
    background: var(--rule-grey);
  }
  .contact {
    position: absolute;
    left: 362px; top: 48px;
    width: 225px;
    color: var(--maroon);
  }
  .contact-name { font-size: 22px; letter-spacing: 1px; text-transform: uppercase; font-weight: 700; white-space: nowrap; }
  .contact-role { font-size: 14px; margin-top: 2px; }
  .contact-address { font-size: 15px; line-height: 20px; margin-top: 16px; font-style: normal; }
  .contact-phone {
    font-size: 15px; margin-top: 6px;
    display: flex; align-items: center; gap: 8px;
  }
  .contact-phone svg { width: 11px; height: 11px; fill: var(--maroon); }
</style>
</head>
<body>
  <section class="card card-back">
    <ul class="service-list">
      <li>Roads</li>
      <li>Substation Pads</li>
      <li>Temporary Pads</li>
      <li>Site Pads</li>
      <li>Land Leveling</li>
      <li>Powerline Row Cleaning</li>
      <li>Land Clearing</li>
      <li>Gates</li>
      <li>Fencing</li>
      <li>Construction Entrances</li>
      <li>Excavation</li>
      <li>Trenching</li>
      <li>Underground Utilities</li>
      <li>Directional Boring</li>
      <li>Pile Driving</li>
    </ul>
    <div class="brand">
      <span class="brand-name">Brenner</span>
      <span class="brand-sub">Construction</span>
    </div>
  </section>

  <section class="card card-front">
    <div class="brand">
      <span class="brand-name">Brenner</span>
      <span class="brand-sub">Construction</span>
    </div>
    <div class="divider"></div>
    <div class="contact">
      <div class="contact-name">Danny Brenner</div>
      <div class="contact-role">Owner</div>
      <address class="contact-address">4837 FM 952, Halden<br>TX 79284</address>
      <div class="contact-phone">
        <svg viewBox="0 0 24 24" aria-hidden="true"><path d="M6.6 10.8c1.4 2.8 3.8 5.1 6.6 6.6l2.2-2.2c.3-.3.7-.4 1-.2 1.1.4 2.3.6 3.6.6.6 0 1 .4 1 1V20c0 .6-.4 1-1 1C10.6 21 3 13.4 3 4c0-.6.4-1 1-1h3.5c.6 0 1 .4 1 1 0 1.3.2 2.5.6 3.6.1.3 0 .7-.2 1l-2.3 2.2z"/></svg>
        <span>(325) 518-2906</span>
      </div>
    </div>
    <div class="front-band"></div>
  </section>
</body>
</html>
```